OLU58 biz card & Stationery

LU58 is a personalized shopping experience brought to you, that lets you find and discover fashion goods through a collection of boutiques curated by taste-makers - celebrities, stylists, designers, and fashion bloggers. Boutiques uses visual technology to help fashionistas discover and shop their look and creates the opportunity for designers to showcase their collections and latest inspirations online.

OLU58 is built on technology developed by our team of fashion experts who work with engineers to “teach” our computer systems to understand various patterns, pairings, and genre definitions. When signed into your account, OLU58 learns about your style and preferences and in turn, provides you better results and recommendations over time. Ultimately, OLU58 will provide shoppers with a much richer and interactive shopping experience and help drive traffic to retailers' websites.

We need a definitely cool business card. The card must be black! And must use our official logo which can be download from OLU58.com

The address for Letter head and evenlop, please use 4872 Crestwick Parkway, Sutie 510 Los Angeles CA90412, email will be anyone@OLU58.com, website is www.OLU58.com

thanks

We received some of the design, thanks. But most of the design are not what we want. We need a very clean version with black ground, you may also use some dark gray to add the element. please take a look at http://morvalstudio.no/work/#pelter__ostrama/, we do like this kind of design very much. hope it help.

```html
<!DOCTYPE html>
<html lang="en">
<head>
<meta charset="utf-8">
<title>OLU58 Stationery</title>
<link rel="stylesheet" href="https://fonts.googleapis.com/css2?family=Lato:wght@400;700&family=Tinos&family=Arimo:wght@700&display=swap">
<style>
  :root {
    --backdrop: #c6c6c6;
    --paper: #ffffff;
    --ink: #000000;
    --card-text: #e6e6e6;
    --card-muted: #9a9a9a;
  }
  html, body { margin: 0; padding: 0; overflow: hidden; }
  body {
    width: 1200px; height: 900px; position: relative;
    background: var(--backdrop);
    font-family: "Lato", Arial, sans-serif;
  }
  .sheet { position: absolute; overflow: hidden; box-shadow: 6px 8px 10px rgba(0,0,0,0.25); }

  /* Brand name placeholder: one colour, one weight, one plain square */
  .brand-mark {
    position: absolute; display: flex; align-items: center;
    color: var(--ink); font-family: "Lato", Arial, sans-serif; font-weight: 400; line-height: 1;
  }
  .brand-square { background: var(--ink); flex: none; }

  /* Letterhead */
  .letterhead { left: 114px; top: 76px; width: 570px; height: 714px; background: var(--paper); }
  .letterhead .brand-mark { left: 34px; top: 42px; font-size: 44px; gap: 12px; }
  .letterhead .brand-square { width: 30px; height: 30px; }
  .letterhead-footer {
    position: absolute; left: 0; bottom: 0; width: 100%; height: 56px;
    background: var(--ink); color: var(--paper); text-align: center;
    font-size: 13px; line-height: 17px; padding-top: 3px; box-sizing: border-box;
    letter-spacing: 0.3px;
  }

  /* Envelope */
  .envelope { left: 360px; top: 360px; width: 696px; height: 326px; background: var(--paper); }
  .envelope .brand-mark { left: 38px; top: 22px; font-size: 26px; gap: 8px; }
  .envelope .brand-square { width: 18px; height: 18px; }
  .envelope-address {
    position: absolute; left: 160px; top: 18px; font-style: normal;
    font-family: "Tinos", "Times New Roman", serif; font-size: 14px; line-height: 21px; color: var(--ink);
  }
  .envelope-url {
    position: absolute; left: 176px; top: 292px;
    font-family: "Arimo", Arial, sans-serif; font-weight: 700; font-size: 22px; color: var(--ink);
  }

  /* Business card */
  .business-card { left: 780px; top: 106px; width: 284px; height: 162px; background: var(--ink); }
  .card-name {
    position: absolute; right: 12px; top: 12px; text-align: right; color: var(--card-text);
    font-size: 20px; line-height: 22px;
  }
  .card-role { display: block; font-size: 12px; line-height: 14px; color: var(--card-muted); }
  .card-contact {
    position: absolute; right: 12px; top: 102px; text-align: right; color: var(--card-muted);
    font-size: 7px; line-height: 10px;
  }
</style>
</head>
<body>

<section class="sheet letterhead">
  <div class="brand-mark"><span class="brand-square"></span><span>OLU58</span></div>
  <footer class="letterhead-footer">
    - 4872 Crestwick Parkway, Sutie 510 Los Angeles Ca90412 -<br>
    (801) 555-0142<br>
    www.OLU58.com
  </footer>
</section>

<section class="sheet envelope">
  <div class="brand-mark"><span class="brand-square"></span><span>OLU58</span></div>
  <address class="envelope-address">
    4872 Crestwick Parkway,<br>
    Sutie 510 Los Angeles Ca90412
  </address>
  <div class="envelope-url">www.OLU58.com</div>
</section>

<section class="sheet business-card">
  <div class="card-name">Mara Lind<span class="card-role">creative director</span></div>
  <div class="card-contact">
    4872 Crestwick Parkway,<br>
    Sutie 510 Los Angeles Ca90412<br>
    Mobile 555-0142<br>
    anyone@OLU58.com<br>
    www.OLU58.com
  </div>
</section>

</body>
</html>
```